Corvelle BSH Book Cover Design: Book 1 of 4

Designers must not submit more than 1 design. Submission of multiple designs will result in disqualification.

Designer must be highly experienced with properly designing and formatting Corvelle BSH book covers. The winner of this contest will receive three more covers to do. This project is for one of four books in a series. I want the same designer to do all four books because they are in a series and need to look the same. Attached are the directions and files.

Target Market(s)

see attachments

Industry/Entity Type

see attachments

Requirements
Must have
• see attachments
Nice to have
• see attachments
Should not have
• see attachments

```html
<!DOCTYPE html>
<html lang="en">
<head>
<meta charset="utf-8">
<title>Know The Hull – Cover Wrap</title>
<link href="https://fonts.googleapis.com/css2?family=Bebas+Neue&family=Montserrat:wght@400;500;600;700&family=Oswald:wght@300;400&display=swap" rel="stylesheet">
<style>
  :root {
    --navy: #15233a;
    --navy-deep: #0d1828;
    --gold: #b8996a;
    --gold-bright: #d2a55d;
    --ink-light: #e9e7e2;
    --panel: rgba(22, 30, 44, 0.55);
    --panel-box: rgba(40, 44, 52, 0.72);
  }
  * { margin: 0; padding: 0; box-sizing: border-box; }
  html, body { width: 1200px; height: 771px; overflow: hidden; background: var(--navy-deep); }
  .cover {
    position: relative; width: 1200px; height: 771px; overflow: hidden;
    font-family: "Montserrat", sans-serif; color: var(--ink-light);
  }
  .scene {
    position: absolute; inset: 0;
    background:
      radial-gradient(ellipse 180px 90px at 745px 485px, rgba(255,236,170,0.95), rgba(255,180,80,0.55) 45%, rgba(255,150,60,0) 100%),
      linear-gradient(180deg, #13223a 0%, #1f3450 22%, #4a5464 38%, #a67a48 55%, #e39a45 66%, #c27a36 70%, #4a3a2a 80%, #1b1a1c 100%);
  }
  .scene-boat {
    position: absolute; left: 860px; top: 475px; width: 300px; height: 185px;
    background: radial-gradient(ellipse at 50% 60%, rgba(15,18,26,0.8), rgba(15,18,26,0) 70%);
  }
  /* back */
  .back-panel {
    position: absolute; left: 32px; top: 42px; width: 493px; height: 550px;
    background: var(--panel);
  }
  .tagline { text-align: center; text-transform: uppercase; letter-spacing: 0.02em; }
  .tagline em { color: var(--gold-bright); font-weight: 700; }
  .tagline .rule { display: inline-block; width: 18px; height: 1px; background: currentColor; vertical-align: middle; margin: 0 4px; }
  .back-tagline { position: absolute; left: 32px; width: 493px; top: 59px; font-size: 8px; line-height: 1.25; }
  .title { font-family: "Bebas Neue", sans-serif; white-space: nowrap; line-height: 1; }
  .title .accent { color: var(--gold); }
  .back-title { position: absolute; left: 32px; width: 493px; top: 92px; text-align: center; font-size: 42px; }
  .back-copy { position: absolute; left: 46px; top: 161px; width: 467px; font-size: 9.3px; line-height: 1.22; }
  .back-copy h3 { color: var(--gold); font-weight: 600; font-size: 9.5px; margin-bottom: 3px; }
  .back-copy p { margin-bottom: 6px; text-align: justify; }
  .back-copy ul { list-style: none; margin: 0 0 9px 18px; }
  .back-copy li { margin-bottom: 5.3px; padding-left: 12px; position: relative; }
  .back-copy li::before { content: "·"; position: absolute; left: -4px; }
  .back-copy .series-gap { margin-top: 8px; }
  /* spine */
  .spine-title, .spine-author, .spine-creds {
    position: absolute; transform-origin: left top; transform: rotate(90deg); white-space: nowrap;
  }
  .spine-title { left: 612px; top: 58px; font-family: "Bebas Neue", sans-serif; font-size: 26px; }
  .spine-title .accent { color: var(--gold); }
  .spine-mark { position: absolute; left: 591px; top: 525px; }
  .spine-author { left: 611px; top: 553px; font-family: "Bebas Neue", sans-serif; font-size: 16px; }
  .spine-creds { left: 594px; top: 560px; font-family: "Oswald", sans-serif; font-weight: 300; font-size: 4px; opacity: 0.7; }
  /* front */
  .front-tagline { position: absolute; left: 700px; width: 436px; top: 50px; font-size: 12px; line-height: 1.25; }
  .front-tagline .rule { width: 26px; }
  .front-title { position: absolute; left: 674px; width: 490px; text-align: center; top: 92px; font-size: 96px; letter-spacing: 0.5px; }
  .subtitle-row { position: absolute; top: 192px; left: 700px; width: 500px; display: flex; align-items: center; gap: 10px; }
  .subtitle { font-weight: 700; font-size: 11px; line-height: 1.25; text-transform: uppercase; }
  .subtitle.left { text-align: right; width: 193px; }
  .subtitle.left span { color: var(--gold-bright); }
  .subtitle::after { content: ""; display: block; width: 20px; height: 1px; background: var(--gold); margin-top: 2px; }
  .subtitle.left::after { margin-left: auto; }
  .features { position: absolute; left: 673px; top: 256px; list-style: none; }
  .feature { display: flex; align-items: center; height: 39.6px; }
  .feature-icon {
    width: 30px; height: 30px; border-radius: 50%; margin-right: 9px; flex: none;
    display: flex; align-items: center; justify-content: center;
  }
  .feature:nth-child(1) .feature-icon { background: #a8471f; }
  .feature:nth-child(2) .feature-icon { background: #b0532a; }
  .feature:nth-child(3) .feature-icon { background: #b86033; }
  .feature:nth-child(4) .feature-icon { background: #c4754a; }
  .feature:nth-child(5) .feature-icon { background: #d08e62; }
  .feature-text { font-weight: 600; font-size: 10px; line-height: 1.18; text-transform: uppercase; }
  .promise-box {
    position: absolute; left: 957px; top: 248px; width: 243px; height: 122px;
    background: var(--panel-box);
  }
  .promise-mark { position: absolute; left: 957px; top: 262px; width: 100px; text-align: center; }
  .promise-text {
    position: absolute; left: 957px; top: 296px; width: 100px; text-align: center;
    font-weight: 600; font-size: 9px; line-height: 1.5; text-transform: uppercase;
  }
  .promise-text span { color: var(--gold); }
  .promise-text::after { content: ""; display: block; width: 38px; height: 1px; background: var(--ink-light); margin: 7px auto 0; }
  .author-rule { position: absolute; left: 955px; top: 652px; width: 200px; height: 1px; background: var(--gold); opacity: 0.7; }
  .author-mark { position: absolute; left: 904px; top: 630px; }
  .author { position: absolute; left: 640px; width: 560px; top: 672px; text-align: center; font-family: "Bebas Neue", sans-serif; font-size: 46px; line-height: 1; }
  .credentials { position: absolute; left: 640px; width: 560px; top: 720px; text-align: center; font-family: "Oswald", sans-serif; font-weight: 300; font-size: 13px; letter-spacing: 0.5px; }
</style>
</head>
<body>
<div class="cover">
  <div class="scene" role="img" aria-label="Sunset over a calm bay with a cable-stayed bridge and a bowrider boat cruising toward the viewer"></div>
  <div class="scene-boat" role="img" aria-label="Dark-hulled bowrider boat with bimini top"></div>

  <!-- Back cover -->
  <div class="back-panel"></div>
  <div class="tagline back-tagline"><span class="rule"></span>The smart buyer's guide to finding<span class="rule"></span><br>The right <em>boat</em> and boating with confidence</div>
  <div class="title back-title">Know The <span class="accent">Hull</span></div>
  <div class="back-copy">
    <h3>Know The Hull:</h3>
    <p>Before you spend thousands on a boat… spend a few hours learning what experienced boaters wish they knew.</p>
    <p>Buying a recreational boat is exciting—but it can also be expensive, confusing, and full of costly mistakes.</p>
    <p>This practical guide helps first-time buyers understand how to evaluate boats, compare ownership options, recognize hidden costs, and avoid expensive surprises before signing the paperwork. Through easy-to-follow explanations, checklists, comparison tables, and illustrations, you'll gain the confidence to make informed decisions and purchase a boat that truly fits your lifestyle.</p>
    <p>Whether you're shopping for your first boat or upgrading to your next one, this book will help you buy smarter and avoid the mistakes that many owners only discover after it's too late.</p>
    <h3>You'll Learn How To:</h3>
    <ul>
      <li>Choose the right boat</li>
      <li>Compare ownership options</li>
      <li>Inspect boats with confidence</li>
      <li>Understand engines and systems</li>
      <li>Estimate ownership costs</li>
      <li>Avoid common buying mistakes</li>
      <li>Know when to hire a surveyor</li>
      <li>Negotiate from an informed position</li>
    </ul>
    <h3>About the Author</h3>
    <p>Captain Dale R. Anders is a U.S. Coast Guard Licensed Captain, certified boating instructor, military veteran, and experienced recreational boater. Having trained thousands of students and delivered hundreds of vessels, he created the Dockside Smarts series to help new boaters avoid costly mistakes and enjoy safer, more rewarding time on the water.</p>
    <h3 class="series-gap">Series Tagline</h3>
    <p>The Dockside Smarts Series<br>Helping new recreational boaters make smarter decisions before buying, boating, and traveling.</p>
  </div>

  <!-- Spine -->
  <div class="spine-title">Know The <span class="accent">Hull</span></div>
  <svg class="spine-mark" width="18" height="18" viewBox="0 0 18 18" aria-hidden="true"><circle cx="9" cy="9" r="6" fill="none" stroke="#e9e7e2" stroke-width="1.4"/></svg>
  <div class="spine-author">By Captain Dale R. Anders</div>
  <div class="spine-creds">USCG Captain • Instructor • Veteran</div>

  <!-- Front cover -->
  <div class="tagline front-tagline"><span class="rule"></span> The smart buyer's guide to finding <span class="rule"></span><br>The right <em>boat</em> and boating with confidence</div>
  <div class="title front-title">Know The <span class="accent">Hull</span></div>
  <div class="subtitle-row">
    <div class="subtitle left">A complete guide for<br><span>first time boat buyers</span></div>
    <svg width="34" height="40" viewBox="0 0 34 40" aria-hidden="true">
      <g fill="none" stroke="#e9e7e2" stroke-width="2.2" stroke-linecap="round">
        <circle cx="17" cy="5" r="3"/><line x1="17" y1="8" x2="17" y2="36"/><line x1="10" y1="13" x2="24" y2="13"/>
        <path d="M4 24 Q6 36 17 37 Q28 36 30 24"/>
      </g>
    </svg>
    <div class="subtitle right">From shopping to sea<br>trial and beyond</div>
  </div>

  <ul class="features">
    <li class="feature"><span class="feature-icon"><svg width="18" height="18" viewBox="0 0 18 18"><circle cx="7.5" cy="7.5" r="5" fill="none" stroke="#fff" stroke-width="1.8"/><line x1="11" y1="11" x2="16" y2="16" stroke="#fff" stroke-width="2.2" stroke-linecap="round"/></svg></span><span class="feature-text">Find the right boat for<br>your needs and budget</span></li>
    <li class="feature"><span class="feature-icon"><svg width="20" height="20" viewBox="0 0 20 20"><circle cx="10" cy="10" r="8" fill="none" stroke="#fff" stroke-width="1.4"/><path d="M5.5 10 L9 13.5 L15 6" fill="none" stroke="#fff" stroke-width="1.8" stroke-linecap="round"/></svg></span><span class="feature-text">Shop smart<br>and avoid red flags</span></li>
    <li class="feature"><span class="feature-icon"><svg width="18" height="18" viewBox="0 0 18 18"><path d="M9 2 L9 13 L3 13 Z M10 4 L15 13 L10 13 Z" fill="#fff"/><path d="M2 14.5 L16 14.5 L14 16.5 L4 16.5 Z" fill="#fff"/></svg></span><span class="feature-text">Sea trial like a pro</span></li>
    <li class="feature"><span class="feature-icon"><svg width="16" height="18" viewBox="0 0 16 18"><rect x="2" y="2.5" width="12" height="14" rx="1.5" fill="none" stroke="#fff" stroke-width="1.3"/><rect x="5.5" y="1" width="5" height="3" fill="#fff"/><line x1="5" y1="8" x2="11" y2="8" stroke="#fff"/><line x1="5" y1="11" x2="11" y2="11" stroke="#fff"/><line x1="5" y1="14" x2="11" y2="14" stroke="#fff"/></svg></span><span class="feature-text">Inspections, survey<br>&amp; negotiations</span></li>
    <li class="feature"><span class="feature-icon"><svg width="14" height="18" viewBox="0 0 14 18"><text x="7" y="15" text-anchor="middle" font-family="Montserrat, sans-serif" font-weight="700" font-size="17" fill="#fff">$</text></svg></span><span class="feature-text">Understand true<br>ownership cost</span></li>
  </ul>

  <div class="promise-box"></div>
  <div class="promise-mark">
    <svg width="66" height="26" viewBox="0 0 66 26" aria-hidden="true"><line x1="4" y1="13" x2="18" y2="13" stroke="#e9e7e2" stroke-width="1"/><line x1="48" y1="13" x2="62" y2="13" stroke="#e9e7e2" stroke-width="1"/><circle cx="33" cy="13" r="11" fill="none" stroke="#e9e7e2" stroke-width="1.6"/><path d="M38 8 L35 15 L28 18 L31 11 Z" fill="none" stroke="#e9e7e2" stroke-width="1.3"/></svg>
  </div>
  <div class="promise-text">Avoid costly<br>mistakes<br>buy with<br><span>confidence</span></div>

  <div class="author-rule"></div>
  <svg class="author-mark" width="34" height="34" viewBox="0 0 34 34" aria-hidden="true"><circle cx="17" cy="17" r="11" fill="none" stroke="#b8996a" stroke-width="2"/><circle cx="17" cy="17" r="4" fill="none" stroke="#b8996a" stroke-width="1.6"/></svg>
  <div class="author">By Captain Dale R. Anders</div>
  <div class="credentials">USCG-LICENSED CAPTAIN ● CERTIFIED BOATING INSTRUCTOR ● VETERAN</div>
</div>
</body>
</html>
```